Business Card Design

I would like a logo created for the top left corner of the card please. I would like a checkerboard in a dark navy with the edges fading out and one random bright orange square.
Updates

I have attached some further notes and a really rough sketch of what I am after.  Thank you. :)

Target Market(s)

Construction, mining, mechanical

Industry/Entity Type

Business

Contact Information for Business Card

Korvane Works Pty Ltd, Glen Hadwick, P. 0418365072, F. 0736209158, E.glen@korvaneworks.com.au, PO Box 87 YARRAWONGA Q 4581, ABN 53209874611

Font styles to use
Sans Serif

Requirements
Must have
• Really Dark Navy
Really bright Orange

```html
<!DOCTYPE html>
<html lang="en">
<head>
<meta charset="utf-8">
<title>Korvane Works – Business Card</title>
<link rel="stylesheet" href="https://fonts.googleapis.com/css2?family=Open+Sans:wght@600;700;800&display=swap">
<style>
  :root {
    --navy: #0f2a55;
    --orange: #f7a600;
    --card: #ffffff;
    --backdrop: #2b2b2b;
    --mark-soft: #c9d0dc;
  }
  * { margin: 0; padding: 0; box-sizing: border-box; }
  html, body {
    width: 1200px;
    height: 849px;
    overflow: hidden;
    background: var(--backdrop);
    font-family: "Open Sans", Arial, sans-serif;
  }
  .business-card {
    position: absolute;
    left: 150px;
    top: 148px;
    width: 900px;
    height: 553px;
    background: var(--card);
    color: var(--navy);
    overflow: hidden;
  }
  .symbol-area {
    position: absolute;
    left: 43px;
    top: 37px;
    width: 228px;
    height: 228px;
    background: radial-gradient(circle at 50% 50%, var(--mark-soft) 0%, var(--mark-soft) 55%, rgba(201,208,220,0) 100%);
  }
  .wordmark {
    position: absolute;
    right: 50px;
    top: 62px;
    display: flex;
    align-items: center;
    gap: 14px;
  }
  .wordmark-square {
    width: 22px;
    height: 22px;
    background: var(--orange);
  }
  .wordmark-name {
    font-size: 46px;
    font-weight: 800;
    color: var(--navy);
    letter-spacing: -0.5px;
    line-height: 1;
    white-space: nowrap;
  }
  .holder {
    position: absolute;
    right: 50px;
    top: 300px;
    text-align: center;
  }
  .holder-name {
    font-size: 42px;
    font-weight: 700;
    line-height: 1.2;
    white-space: nowrap;
  }
  .holder-phone {
    font-size: 28px;
    font-weight: 700;
    line-height: 1.3;
    white-space: nowrap;
  }
  .contact-details {
    position: absolute;
    left: 43px;
    top: 330px;
    list-style: none;
    font-size: 21px;
    font-weight: 700;
    line-height: 31px;
    white-space: nowrap;
  }
  .accent-band {
    position: absolute;
    left: 0;
    bottom: 0;
    width: 100%;
    height: 54px;
    background: var(--orange);
  }
</style>
</head>
<body>
  <div class="business-card">
    <div class="symbol-area" role="img" aria-label="Space for the company symbol"></div>

    <div class="wordmark">
      <span class="wordmark-square"></span>
      <span class="wordmark-name">Korvane Works</span>
    </div>

    <div class="holder">
      <p class="holder-name">Glen Hadwick</p>
      <p class="holder-phone">0418 365 072</p>
    </div>

    <ul class="contact-details">
      <li>PO Box 87 YARRAWONGA Q 4581</li>
      <li>P. 0418 365 072</li>
      <li>F. 07 3620 9158</li>
      <li>E. glen@korvaneworks.com.au</li>
      <li>ABN 53 209 874 611</li>
    </ul>

    <div class="accent-band"></div>
  </div>
</body>
</html>
```